MSA Plans

I would like to rebuild my brochure for the 3 business plans that I currently offer my clients. I would like to make it look much more modern & attractive to clients when choosing one of our service plans. If we can stick to a tech theme that would be great. Message me for anymore information.

```html
<!DOCTYPE html>
<html lang="en">
<head>
<meta charset="utf-8">
<title>Brightline IT – Managed Services Framework</title>
<link rel="stylesheet" href="https://fonts.googleapis.com/css2?family=Montserrat:ital,wght@0,700;1,400&family=Oswald:wght@400;500&family=Roboto:wght@400;700&display=swap">
<style>
:root{
  --bg:#e3e3e3;
  --orange:#f26522;
  --orange-light:#f8a539;
  --price-cell:#c4420f;
  --ink:#1b1b1b;
  --footer:#3c3c3c;
  --pill:#4a4a4a;
  --col:#efefef;
  --col-alt:#f5f5f5;
  --rule:#c9c9c9;
  --text:#333;
  --green:#6cbf3b;
  --red:#e21d1d;
  --white:#fff;
}
*{margin:0;padding:0;box-sizing:border-box}
html,body{width:1200px;height:1200px;overflow:hidden;background:var(--bg)}
body{position:relative;font-family:"Roboto",sans-serif;color:var(--text)}
.page{position:absolute;width:373px;height:528px;background:var(--white);overflow:hidden}
.page--cover{left:431px;top:58px}
.page--msa{left:209px;top:612px}
.page--cyber{left:617px;top:615px}
.layer{position:absolute;left:0;top:0}

/* cover */
.brand{position:absolute;left:38px;top:352px;display:flex;align-items:center;gap:5px;font-family:"Montserrat",sans-serif;font-weight:700;font-size:13px;color:var(--ink);letter-spacing:.3px}
.brand__mark{width:9px;height:9px;background:var(--orange)}
.cover-title{position:absolute;left:148px;top:326px;font-family:"Montserrat",sans-serif;font-weight:700;font-size:23px;line-height:21.5px;color:var(--orange);letter-spacing:.2px}
.cover-rule{position:absolute;top:401px;height:1.5px;background:var(--orange-light)}
.cover-rule--thick{left:30px;width:107px;height:4px;top:399px;background:var(--orange)}
.cover-rule--thin{left:137px;width:205px}
.cover-abn{position:absolute;left:41px;top:410px;font-family:"Oswald",sans-serif;font-weight:500;font-size:11.5px;color:var(--orange)}
.cover-tagline{position:absolute;left:148px;top:410px;font-family:"Montserrat",sans-serif;font-style:italic;font-size:10.6px;line-height:13.5px;color:var(--ink)}
.cover-contact{position:absolute;font-family:"Oswald",sans-serif;color:var(--orange);font-size:7.2px;line-height:12.5px}
.cover-contact--left{left:17px;top:484px}
.cover-contact--right{right:26px;top:483px;text-align:right}
.cover-contact--right .phone{font-size:9.4px}
.cover-contact .ico{display:inline-block;width:5px;height:4px;background:#9a9a9a;margin-right:4px;vertical-align:middle}
.cover-contact .ico-r{display:inline-block;width:4px;height:5px;background:#9a9a9a;margin-left:4px;vertical-align:middle;border-radius:50%}

/* plan tables */
.card{position:absolute;left:35px;width:303px;background:var(--white);border-radius:6px 6px 0 0;box-shadow:0 0 4px rgba(0,0,0,.08)}
.page--msa .card{top:35px;height:402px}
.page--cyber .card{top:36px;height:302px}
.card__head{position:relative;height:27px;background:var(--orange);border-radius:6px 6px 0 0;color:var(--white)}
.card__title{position:absolute;left:18px;top:5px;font-family:"Oswald",sans-serif;font-weight:500;font-size:11.5px;letter-spacing:.1px}
.card__plan{position:absolute;top:10px;width:60px;margin-left:-30px;text-align:center;font-family:"Oswald",sans-serif;font-size:6.8px}
.col{position:absolute;top:27px;bottom:0}
.row{position:relative;height:13.3px;font-size:6.2px}
.row--2{height:25px}
.row--1{height:15.7px}
.label{position:absolute;left:18px;width:147px;top:0;bottom:1px;display:flex;align-items:center;line-height:7.6px;border-bottom:.6px solid var(--rule);color:var(--text)}
.cell{position:absolute;top:0;bottom:1px;width:40px;display:flex;align-items:center;justify-content:center;border-bottom:.6px solid var(--rule);font-weight:700;font-size:5px;line-height:5.6px;text-align:center;color:var(--ink)}
.cell svg{width:8px;height:7px}
.msa .c1{left:172px}.msa .c2{left:214px}.msa .c3{left:257px}
.cyber .label{width:148px}
.cyber .c1{left:180px;width:46px}.cyber .c2{left:245px;width:46px}
.section{position:relative;margin-top:4px}
.pill{position:relative;left:-5px;width:107px;height:15px;margin-bottom:5px;background:var(--pill);border-radius:0 8px 8px 0;color:var(--white);font-family:"Oswald",sans-serif;font-size:8.6px;line-height:15px;padding-left:23px}
.pill::after{content:"";position:absolute;left:0;top:15px;border-top:4px solid var(--ink);border-left:4px solid transparent}

.price{position:absolute;height:21px;background:var(--orange);color:var(--white);font-family:"Oswald",sans-serif;font-weight:500;clip-path:polygon(0 0,100% 0,100% 100%,12px 100%)}
.page--msa .price{left:110px;top:437px;width:228px}
.page--cyber .price{left:97px;top:338px;width:241px}
.price__label{position:absolute;top:3px;font-size:10px}
.price__cell{position:absolute;top:0;height:21px;background:var(--price-cell);text-align:center;font-size:10px;line-height:21px}
.version{position:absolute;right:35px;text-align:right;font-size:5.4px;line-height:8px;color:var(--ink)}
.page--msa .version{top:462px}
.page--cyber .version{top:364px}

/* footer */
.footer{position:absolute;left:0;bottom:0;width:373px;height:38px}
.footer__mail{position:absolute;left:20px;top:4px;color:var(--white);font-size:5.3px;line-height:11px}
.footer__mail i{display:inline-block;width:5px;height:3.5px;background:var(--orange);margin-right:4px;vertical-align:middle}
.footer__name{position:absolute;left:123px;width:141px;top:2px;text-align:center;font-family:"Oswald",sans-serif;font-weight:500;font-size:7.4px;line-height:8.6px;color:var(--orange)}
.footer__name b{font-weight:500;color:var(--ink)}
.footer__abn{position:absolute;left:123px;width:141px;top:22px;text-align:center;font-family:"Oswald",sans-serif;font-size:7.6px;color:var(--white)}
.footer__call{position:absolute;right:14px;top:5px;text-align:right;color:var(--white);font-family:"Oswald",sans-serif}
.footer__call .phone{font-size:9.2px;line-height:12px}
.footer__call .addr{font-size:5.2px;line-height:9px}
.footer__call i{display:inline-block;width:3.5px;height:4.5px;background:var(--orange);border-radius:50%;margin-left:4px;vertical-align:middle}
</style>
</head>
<body>

<svg width="0" height="0" style="position:absolute" aria-hidden="true">
  <symbol id="tick" viewBox="0 0 10 8"><path d="M1 4.3 3.7 6.8 9 1" fill="none" stroke="#6cbf3b" stroke-width="1.5" stroke-linecap="round" stroke-linejoin="round"/></symbol>
  <symbol id="cross" viewBox="0 0 10 8"><path d="M2.5 1 7.5 7M7.5 1 2.5 7" fill="none" stroke="#e21d1d" stroke-width="1.6" stroke-linecap="round"/></symbol>
  <linearGradient id="orangeFade" x1="0" y1="0" x2="1" y2="0"><stop offset="0" stop-color="#f26522"/><stop offset="1" stop-color="#f8a539"/></linearGradient>
  <linearGradient id="orangeFadeV" x1="0" y1="0" x2="1" y2="1"><stop offset="0" stop-color="#f8a539"/><stop offset="1" stop-color="#f26522"/></linearGradient>
  <radialGradient id="techGlow" cx=".62" cy=".55" r=".7"><stop offset="0" stop-color="#8fc8ec"/><stop offset=".3" stop-color="#2b6fa3"/><stop offset=".7" stop-color="#0f2c4d"/><stop offset="1" stop-color="#081526"/></radialGradient>
</svg>

<!-- cover -->
<section class="page page--cover">
  <svg class="layer" width="373" height="528" role="img" aria-label="Photograph of a hand holding a glowing laptop surrounded by a digital network of connected icons">
    <path d="M0 0H373V294C260 250 110 212 0 215Z" fill="url(#techGlow)"/>
  </svg>
  <svg class="layer" width="373" height="528" aria-hidden="true">
    <path d="M0 215C110 212 260 250 373 294V358C300 318 170 276 0 275Z" fill="url(#orangeFade)"/>
    <path d="M0 460C130 468 260 448 373 436V459C280 472 190 500 128 528H0Z" fill="var(--ink)"/>
  </svg>
  <div class="brand"><span class="brand__mark"></span>BRIGHTLINE</div>
  <h1 class="cover-title">MANAGED<br>SERVICES<br>FRAMEWORK</h1>
  <div class="cover-rule cover-rule--thick"></div>
  <div class="cover-rule cover-rule--thin"></div>
  <p class="cover-abn">ABN: 41 208 375 916</p>
  <p class="cover-tagline">Defining our services and how we<br>deliver these consistently to you.</p>
  <div class="cover-contact cover-contact--left">
    <div><span class="ico"></span>brightlineit.com.au</div>
    <div><span class="ico"></span>service@brightlineit.com.au</div>
  </div>
  <div class="cover-contact cover-contact--right">
    <div class="phone">1300 555 019<span class="ico-r"></span></div>
    <div>12/48 Harbour Lane, Westfield VIC 3150<span class="ico-r"></span></div>
  </div>
</section>

<!-- managed services agreement -->
<section class="page page--msa msa">
  <svg class="layer" width="373" height="528" aria-hidden="true">
    <path d="M318 0H373V100L290 170Z" fill="url(#orangeFadeV)"/>
    <path d="M0 400Q60 365 120 340H220L120 460Q96 476 82 490H0Z" fill="var(--orange)"/>
  </svg>
  <div class="card">
    <div class="col" style="left:172px;width:40px;background:var(--col)"></div>
    <div class="col" style="left:214px;width:40px;background:var(--col)"></div>
    <div class="col" style="left:257px;width:40px;background:var(--col)"></div>
    <div class="card__head">
      <h2 class="card__title">MANAGED SERVICES AGREEMENT</h2>
      <span class="card__plan" style="left:192px">ESSENTIAL</span>
      <span class="card__plan" style="left:234px">BUSINESS</span>
      <span class="card__plan" style="left:280px">PROFESSIONAL</span>
    </div>

    <div class="section" style="margin-top:2px">
      <div class="pill">SUPPORT</div>
      <div class="row"><span class="label">Unlimited Remote Support 7am to 6pm</span><span class="cell c1"><svg><use href="#tick"/></svg></span><span class="cell c2"><svg><use href="#tick"/></svg></span><span class="cell c3"><svg><use href="#tick"/></svg></span></div>
      <div class="row"><span class="label">3rd Party Vendor Support</span><span class="cell c1"><svg><use href="#tick"/></svg></span><span class="cell c2"><svg><use href="#tick"/></svg></span><span class="cell c3"><svg><use href="#tick"/></svg></span></div>
      <div class="row"><span class="label">Reactive Onsite Support 8am to 5pm VIP Rates</span><span class="cell c1">VIP Rates</span><span class="cell c2"><svg><use href="#tick"/></svg></span><span class="cell c3"><svg><use href="#tick"/></svg></span></div>
      <div class="row"><span class="label">After-Hours Support</span><span class="cell c1">VIP Rates</span><span class="cell c2">VIP Rates</span><span class="cell c3"><svg><use href="#tick"/></svg></span></div>
    </div>

    <div class="section">
      <div class="pill">SERVICE</div>
      <div class="row"><span class="label">Guaranteed SLA Response Times</span><span class="cell c1"><svg><use href="#tick"/></svg></span><span class="cell c2"><svg><use href="#tick"/></svg></span><span class="cell c3"><svg><use href="#tick"/></svg></span></div>
      <div class="row"><span class="label">24x7 Website &amp; Infrastructure Monitoring</span><span class="cell c1"><svg><use href="#tick"/></svg></span><span class="cell c2"><svg><use href="#tick"/></svg></span><span class="cell c3"><svg><use href="#tick"/></svg></span></div>
      <div class="row"><span class="label">Secure Web Content Filtering</span><span class="cell c1"><svg><use href="#tick"/></svg></span><span class="cell c2"><svg><use href="#tick"/></svg></span><span class="cell c3"><svg><use href="#tick"/></svg></span></div>
      <div class="row"><span class="label">Backup Monitoring</span><span class="cell c1"><svg><use href="#tick"/></svg></span><span class="cell c2"><svg><use href="#tick"/></svg></span><span class="cell c3"><svg><use href="#tick"/></svg></span></div>
      <div class="row"><span class="label">Workstation OS Patching &amp; Updating</span><span class="cell c1"><svg><use href="#tick"/></svg></span><span class="cell c2"><svg><use href="#tick"/></svg></span><span class="cell c3"><svg><use href="#tick"/></svg></span></div>
      <div class="row"><span class="label">CEO / MD Home Tech Support</span><span class="cell c1"><svg><use href="#tick"/></svg></span><span class="cell c2"><svg><use href="#tick"/></svg></span><span class="cell c3"><svg><use href="#tick"/></svg></span></div>
      <div class="row"><span class="label">Monthly Tech Site Visit</span><span class="cell c1"><svg><use href="#cross"/></svg></span><span class="cell c2">Quarterly</span><span class="cell c3">Monthly</span></div>
      <div class="row"><span class="label">Short Term Loan Equipment</span><span class="cell c1"><svg><use href="#cross"/></svg></span><span class="cell c2">1 Month</span><span class="cell c3">3 Month</span></div>
      <div class="row"><span class="label">Adds / Moves / Changes (Staff)</span><span class="cell c1"><svg><use href="#tick"/></svg></span><span class="cell c2"><svg><use href="#tick"/></svg></span><span class="cell c3"><svg><use href="#tick"/></svg></span></div>
      <div class="row"><span class="label">Adds / Moves / Changes (Workstations)</span><span class="cell c1">VIP Rates</span><span class="cell c2">VIP Rates</span><span class="cell c3"><svg><use href="#tick"/></svg></span></div>
    </div>

    <div class="section">
      <div class="pill">MANAGEMENT</div>
      <div class="row"><span class="label">Asset and Warranty Tracking &amp; Reporting</span><span class="cell c1"><svg><use href="#tick"/></svg></span><span class="cell c2"><svg><use href="#tick"/></svg></span><span class="cell c3"><svg><use href="#tick"/></svg></span></div>
      <div class="row"><span class="label">Comprehensive IT Documentation</span><span class="cell c1"><svg><use href="#tick"/></svg></span><span class="cell c2"><svg><use href="#tick"/></svg></span><span class="cell c3"><svg><use href="#tick"/></svg></span></div>
      <div class="row"><span class="label">Technology Strategy Meeting</span><span class="cell c1">Annual</span><span class="cell c2">Quarterly</span><span class="cell c3">Monthly</span></div>
      <div class="row"><span class="label">Technology Business Review Meeting</span><span class="cell c1">Annual</span><span class="cell c2">Bi Annual</span><span class="cell c3">Quarterly</span></div>
      <div class="row"><span class="label">IT Policy Templates</span><span class="cell c1"><svg><use href="#cross"/></svg></span><span class="cell c2"><svg><use href="#tick"/></svg></span><span class="cell c3"><svg><use href="#tick"/></svg></span></div>
    </div>

    <div class="section">
      <div class="pill">TRAINING</div>
      <div class="row"><span class="label">End User Training Materials</span><span class="cell c1"><svg><use href="#cross"/></svg></span><span class="cell c2"><svg><use href="#cross"/></svg></span><span class="cell c3"><svg><use href="#tick"/></svg></span></div>
      <div class="row"><span class="label">Security Awareness Training</span><span class="cell c1"><svg><use href="#tick"/></svg></span><span class="cell c2"><svg><use href="#tick"/></svg></span><span class="cell c3"><svg><use href="#tick"/></svg></span></div>
    </div>
  </div>

  <div class="price">
    <span class="price__label" style="right:138px">RRP / User</span>
    <span class="price__cell" style="left:97px;width:40px">$110</span>
    <span class="price__cell" style="left:139px;width:40px">$130</span>
    <span class="price__cell" style="left:182px;width:46px">$165</span>
  </div>
  <p class="version">Version 1.0<br>Updated: April 2024</p>

  <div class="footer">
    <svg class="layer" width="373" height="38" aria-hidden="true">
      <rect x="118" y="21" width="150" height="17" fill="var(--orange)"/>
      <polygon points="0,0 123,0 136,19 128,38 0,38" fill="var(--footer)"/>
      <polygon points="260,0 373,0 373,38 252,38 244,19" fill="var(--footer)"/>
    </svg>
    <div class="footer__mail"><div><i></i>brightlineit.com.au</div><div><i></i>service@brightlineit.com.au</div></div>
    <div class="footer__name">BRIGHTLINE IT<br>SERVICES <b>PTY LTD</b></div>
    <div class="footer__abn">ABN: 41 208 375 916</div>
    <div class="footer__call"><div class="phone">1300 555 019<i></i></div><div class="addr">12/48 Harbour Lane, Westfield VIC 3150<i></i></div></div>
  </div>
</section>

<!-- cybersecurity packages -->
<section class="page page--cyber cyber">
  <svg class="layer" width="373" height="528" aria-hidden="true">
    <path d="M317 0H373V100L290 170Z" fill="url(#orangeFadeV)"/>
    <path d="M0 420Q60 380 110 338H200L110 450Q80 474 63 490H0Z" fill="var(--orange)"/>
  </svg>
  <div class="card">
    <div class="col" style="left:172px;width:63px;background:var(--col)"></div>
    <div class="col" style="left:236px;width:67px;background:var(--col-alt)"></div>
    <div class="card__head">
      <h2 class="card__title">CYBERSECURITY PACKAGES</h2>
      <span class="card__plan" style="left:202px">BUSINESS</span>
      <span class="card__plan" style="left:268px">PROFESSIONAL</span>
    </div>
    <div style="height:5px"></div>
    <div class="row row--1"><span class="label">Compliance with NCSB Essential 8 Maturity</span><span class="cell c1">Level 0</span><span class="cell c2">Level 1</span></div>
    <div class="row row--2"><span class="label">Security Standard - Alignment to Brightline<br>Cloud Suite Security Policy &amp; Reporting</span><span class="cell c1"><svg><use href="#tick"/></svg></span><span class="cell c2"><svg><use href="#tick"/></svg></span></div>
    <div class="row row--2"><span class="label">24x7 Security Operations Centre (SOC) -<br>Monitoring Cloud Suite</span><span class="cell c1"><svg><use href="#tick"/></svg></span><span class="cell c2"><svg><use href="#tick"/></svg></span></div>
    <div class="row row--1"><span class="label">Dark Web Scanning</span><span class="cell c1"><svg><use href="#tick"/></svg></span><span class="cell c2"><svg><use href="#tick"/></svg></span></div>
    <div class="row row--1"><span class="label">Cloud Email Filtering</span><span class="cell c1"><svg><use href="#tick"/></svg></span><span class="cell c2"><svg><use href="#tick"/></svg></span></div>
    <div class="row row--1"><span class="label">Cloud Suite Backup</span><span class="cell c1"><svg><use href="#tick"/></svg></span><span class="cell c2"><svg><use href="#tick"/></svg></span></div>
    <div class="row row--1"><span class="label">Automated Email Signatures</span><span class="cell c1"><svg><use href="#tick"/></svg></span><span class="cell c2"><svg><use href="#tick"/></svg></span></div>
    <div class="row row--2"><span class="label">Endpoint Protection with EDR - Workstations &amp;<br>Servers</span><span class="cell c1"><svg><use href="#tick"/></svg></span><span class="cell c2"><svg><use href="#tick"/></svg></span></div>
    <div class="row row--1"><span class="label">3rd Party Applications Updating</span><span class="cell c1"><svg><use href="#cross"/></svg></span><span class="cell c2"><svg><use href="#tick"/></svg></span></div>
    <div class="row row--2"><span class="label">24x7 Security Operations Centre (SOC) -<br>Monitoring Endpoints and Servers</span><span class="cell c1"><svg><use href="#cross"/></svg></span><span class="cell c2"><svg><use href="#tick"/></svg></span></div>
    <div class="row row--2"><span class="label">Privileged Access Management &amp; Application<br>Whitelisting</span><span class="cell c1"><svg><use href="#cross"/></svg></span><span class="cell c2"><svg><use href="#tick"/></svg></span></div>
    <div class="row row--1"><span class="label">Internal Vulnerability Scanning</span><span class="cell c1"><svg><use href="#cross"/></svg></span><span class="cell c2"><svg><use href="#tick"/></svg></span></div>
    <div class="row row--2"><span class="label">Backup &amp; Disaster Recovery to comply with<br>NCSB Essential 8 Maturity Level 1</span><span class="cell c1"><svg><use href="#cross"/></svg></span><span class="cell c2">Pending<br>Assessment</span></div>
  </div>

  <div class="price">
    <span class="price__label" style="right:137px">RRP / User</span>
    <span class="price__cell" style="left:110px;width:63px">$35</span>
    <span class="price__cell" style="left:174px;width:67px">$60</span>
  </div>
  <p class="version">Version 1.0<br>Updated: April 2024</p>

  <div class="footer">
    <svg class="layer" width="373" height="38" aria-hidden="true">
      <rect x="118" y="21" width="150" height="17" fill="var(--orange)"/>
      <polygon points="0,0 123,0 136,19 128,38 0,38" fill="var(--footer)"/>
      <polygon points="260,0 373,0 373,38 252,38 244,19" fill="var(--footer)"/>
    </svg>
    <div class="footer__mail"><div><i></i>brightlineit.com.au</div><div><i></i>service@brightlineit.com.au</div></div>
    <div class="footer__name">BRIGHTLINE IT<br>SERVICES <b>PTY LTD</b></div>
    <div class="footer__abn">ABN: 41 208 375 916</div>
    <div class="footer__call"><div class="phone">1300 555 019<i></i></div><div class="addr">12/48 Harbour Lane, Westfield VIC 3150<i></i></div></div>
  </div>
</section>

</body>
</html>
```